***PLASTIC*** Business Card Design

1 sided business card design
The card will be screen printed on plastic, so colour and fonts must be strong.

Must use the colours in the logo eps attached (Black/Ivory/White). Other colour(s) can be added.

Four (4) examples of how the logo can be printed are included in the logo eps attached.

The business card should highlight the logo. The card will be given to architects, interior designers and builders. It should look sophisticated but also innovative.

Do not cover the whole card with colour as it is important than some of the frosted plastic card is visible.

Be creative.

Target Market(s)

architects, interior designers and builders and wealthy home owners

Industry/Entity Type

Plastic

Requirements
Must have
• Must use the colours in the logo eps attached (Black/Ivory/White). Other colour(s) can be added if necessary.

The font is Square721 ExBT but has been a little thickened. It is not essential that you use this font. The name should be a stronger version of the font than other details.

The card will be printed on PVC - see http://www.vobrelt.com.au/pricelistbcardsplastic.php

Final artwork must be print ready. You must use the printing spec at http://www.vobrelt.com.au/2011%20PVC-TW.pdf

The actual details to be typeset ono the card are:

Rory Pellam

Mobile: 0412 836157
email: info@lumaplastering.com.au
www.lumaplastering.com.au

PO Box 52, Altona, Vic 3018

Plastering | Rendering | Cornicing

```html
<!DOCTYPE html>
<html lang="en">
<head>
<meta charset="utf-8">
<title>Luma Plastering – Business Card</title>
<link href="https://fonts.googleapis.com/css2?family=Saira:wght@300;400;500;700&display=swap" rel="stylesheet">
<style>
  :root {
    --backdrop: #eeeeee;
    --frost: rgba(236, 238, 240, 0.92);
    --frost-edge: #dcdfe2;
    --band-dark: #1f1d1d;
    --band-light: #4a4a4c;
    --ivory: #f3e8cf;
    --white: #ffffff;
    --ink: #2a2a2a;
  }
  html, body {
    margin: 0;
    width: 1200px;
    height: 767px;
    overflow: hidden;
    background: var(--backdrop);
    font-family: "Saira", sans-serif;
  }
  .card {
    position: absolute;
    left: 306px;
    top: 111px;
    width: 663px;
    height: 378px;
    background: var(--frost);
    border: 1px solid var(--frost-edge);
    box-shadow: 0 6px 24px rgba(0,0,0,0.08);
  }
  .brand-band {
    position: absolute;
    left: 0;
    top: 97px;
    width: 582px;
    height: 183px;
    background: linear-gradient(100deg, var(--band-light) 0%, var(--band-dark) 55%, var(--band-dark) 100%);
    border-radius: 0 14px 14px 0;
  }
  .contact {
    position: absolute;
    right: 338px;
    top: 40px;
    text-align: right;
    color: var(--white);
  }
  .contact-name {
    font-size: 21px;
    font-weight: 400;
    line-height: 1;
    margin: 0 0 4px;
  }
  .contact-line {
    font-size: 14px;
    font-weight: 300;
    line-height: 19px;
    margin: 0;
  }
  .contact-phone { margin-bottom: 19px; }
  .divider {
    position: absolute;
    left: 260px;
    top: 34px;
    width: 2px;
    height: 112px;
    background: var(--white);
  }
  .brand-name {
    position: absolute;
    left: 292px;
    top: 46px;
    color: var(--ivory);
    font-weight: 700;
    line-height: 1;
  }
  .brand-name .word-main {
    display: block;
    font-size: 58px;
    letter-spacing: 3px;
  }
  .brand-name .word-sub {
    display: block;
    font-size: 22px;
    letter-spacing: 5.4px;
    margin-top: 6px;
  }
  .services {
    position: absolute;
    left: 156px;
    top: 288px;
    font-size: 15px;
    font-weight: 400;
    letter-spacing: 3.3px;
    color: var(--ink);
    margin: 0;
  }
  .website {
    position: absolute;
    left: 641px;
    top: 188px;
    transform: translate(-50%, -50%) rotate(-90deg);
    font-size: 14px;
    font-weight: 400;
    color: var(--ink);
    white-space: nowrap;
    margin: 0;
  }
</style>
</head>
<body>
  <div class="card">
    <div class="brand-band">
      <div class="contact">
        <p class="contact-name">Rory Pellam</p>
        <p class="contact-line contact-phone">0412 836157</p>
        <p class="contact-line">PO Box 52, Corlin Bay, Orv 5081</p>
        <p class="contact-line">info@lumaplastering.com.au</p>
      </div>
      <div class="divider"></div>
      <div class="brand-name">
        <span class="word-main">LUMA</span>
        <span class="word-sub">PLASTERING</span>
      </div>
    </div>
    <p class="services">Plastering | Rendering | Cornicing</p>
    <p class="website">www.lumaplastering.com.au</p>
  </div>
</body>
</html>
```